Vendor credentialing website for senior living communities - Need totally new design

Veltromark is a company that works on behalf for senior living communities to credential their third party vendors. By utilizing the Veltromark system a senior living community(Assisted Living, Independent Living) will be safer because they now have a way of knowing who the vendors really are that work daily with their residents. The site will be used as a starting point for vendors to use to upload their credentials (i.e criminal background checks, immunization tests, proof of liability insurance, et.) Once the vendor unloads their specific credentials, Veltrormark will check these and a vendor will be given a badge that will allow them to visit all Veltromark partner communities. The site needs to express Veltromark's mission through pictures and tone: Protecting our seniors. Four words that I would use to describe what I am looking for: Clean, Warm, Professional, Simple. Current site www.veltromark.com Let the creative juices flow!

Industry/Entity Type

It Company

```html
<!DOCTYPE html>
<html lang="en">
<head>
<meta charset="utf-8">
<title>Veltromark – Vendor Credentialing for Senior Living</title>
<link rel="stylesheet" href="https://fonts.googleapis.com/css2?family=Lato:wght@300;400;700&display=swap">
<style>
:root{
  --green:#3ea55b;
  --green-dark:#2f8a47;
  --green-deep:#2a7a40;
  --ink:#222;
  --text:#444;
  --muted:#666;
  --white:#fff;
  --paper:#f7f7f7;
  --navy:#2c2f6b;
  --gold:#f5b400;
}
*{box-sizing:border-box;margin:0;padding:0}
html,body{width:1200px;height:3346px;overflow:hidden}
body{font-family:'Lato',sans-serif;color:var(--text);background:var(--white);position:relative}
.wrap{position:absolute;left:0;width:1200px}

/* top bar */
.topbar{top:0;height:45px;background:var(--green);color:var(--white);font-size:13px}
.topbar .contact{position:absolute;left:62px;top:14px;display:flex;gap:34px;align-items:center}
.topbar .contact span{display:flex;align-items:center;gap:9px}
.topbar .checkout{position:absolute;right:62px;top:14px;display:flex;gap:9px;align-items:center}

/* header */
.header{top:45px;height:107px;background:var(--white)}
.brand{position:absolute;left:60px;top:30px;display:flex;align-items:center;gap:14px}
.brand .dot{width:40px;height:40px;border-radius:50%;background:var(--green-deep)}
.brand .name{font-size:36px;font-weight:700;color:var(--green-deep)}
.nav{position:absolute;right:62px;top:60px;display:flex;gap:50px;font-size:14px;color:var(--ink)}
.nav .active{color:var(--green)}

/* hero */
.hero{top:152px;height:403px;background:linear-gradient(90deg,#e9ecec 0%,#d8dcd8 30%,#c9d3dc 62%,#7ea3c4 100%)}
.hero-copy{position:absolute;left:60px;top:100px;width:380px}
.hero-copy .kicker{font-size:28px;font-weight:700;color:var(--green)}
.hero-copy h1{font-size:54px;font-weight:700;color:var(--navy);line-height:1.05}
.hero-copy p{font-size:13px;color:var(--ink);margin-top:4px;line-height:1.3}
.btn-outline{display:inline-block;margin-top:28px;border:2px solid #333;border-radius:4px;padding:10px 16px;font-size:13px;color:var(--ink);background:rgba(255,255,255,.6)}
.dots{position:absolute;left:530px;top:372px;display:flex;gap:12px}
.dots i{width:10px;height:10px;border-radius:50%;background:var(--green-deep)}
.dots i:first-child{background:rgba(255,255,255,.7)}

/* intro */
.intro{top:555px;height:230px;text-align:center}
.section-title{font-size:34px;font-weight:300;color:var(--green)}
.intro .section-title{margin-top:32px}
.intro p{width:1080px;margin:18px auto 0;font-size:13px;line-height:25px;color:var(--ink)}
.btn{display:inline-block;margin-top:32px;width:132px;height:42px;line-height:42px;background:var(--green);color:var(--white);font-size:14px;border-radius:3px}

/* people rows */
.row-title{position:absolute;left:60px;font-size:34px;font-weight:300;color:var(--green)}
.carousel-arrows{position:absolute;right:62px;top:808px;display:flex;gap:22px}
.people{position:absolute;left:0;width:1200px;display:flex}
.person{position:absolute;width:260px;margin-left:-130px;text-align:center;font-size:16px;color:var(--ink)}
.portrait{width:178px;height:178px;border-radius:50%;border:4px solid var(--green);margin:0 auto 36px}
.portrait.light{background:radial-gradient(circle at 50% 40%,#e9d2bf 0%,#c8a58c 38%,#f4f4f4 40%,#e6e6e6 100%)}
.portrait.dark{background:radial-gradient(circle at 50% 42%,#b88b6c 0%,#7a5440 40%,#3d3530 60%,#242424 100%)}

/* video band */
.video{top:1182px;height:337px;background:linear-gradient(90deg,#3c3834 0%,#5e6a70 35%,#8a96a0 60%,#d0c6bc 100%);text-align:center}
.video .shade{position:absolute;inset:0;background:rgba(0,0,0,.25)}
.video h2{position:relative;margin-top:68px;font-size:32px;font-weight:300;color:var(--white)}
.video svg{position:absolute;left:533px;top:146px}

/* benefits */
.benefit{position:absolute;top:1672px;width:360px;margin-left:-180px;text-align:center}
.benefit .icon{width:152px;height:152px;border-radius:50%;background:var(--green);margin:0 auto;display:flex;align-items:center;justify-content:center}
.benefit h3{margin-top:28px;font-size:28px;font-weight:400;color:var(--ink)}
.benefit p{margin-top:18px;font-size:12.5px;line-height:22px;color:var(--ink);padding:0 24px}

/* testimonial */
.testimonial{top:2433px;height:339px;background:linear-gradient(90deg,#6a5a4e 0%,#9c8a7c 35%,#b7a79a 60%,#7a6a60 100%);text-align:center;color:var(--white)}
.testimonial .shade{position:absolute;inset:0;background:rgba(40,35,30,.35)}
.testimonial .inner{position:relative}
.testimonial h2{margin-top:68px;font-size:32px;font-weight:300}
.testimonial p{width:1000px;margin:30px auto 0;font-size:13px;line-height:24px}
.testimonial cite{display:block;margin-top:26px;font-size:13px;font-style:italic}

/* partners */
.partners{top:2772px;height:207px;background:var(--white);display:flex;justify-content:center;align-items:center;gap:48px}
.partner{background:#d8dcd9}

/* footer */
.footer{top:2979px;height:291px;background:var(--green);color:var(--white)}
.footer .brand{left:60px;top:60px}
.footer .brand .dot{width:50px;height:50px;background:#1f5d31}
.footer .brand .name{font-size:46px;color:#1f5d31}
.footer h4{font-size:20px;font-weight:400}
.quick{position:absolute;left:446px;top:48px}
.quick ul{list-style:none;margin-top:18px;font-size:13px;line-height:22px}
.newsletter{position:absolute;left:638px;top:48px;width:300px}
.newsletter p{margin-top:16px;font-size:12px;line-height:16px;color:#9fd8ad}
.newsletter .field{margin-top:20px;width:300px;height:48px;background:var(--white)}
.newsletter .submit{margin-top:20px;display:inline-block;width:84px;height:40px;line-height:40px;text-align:center;background:var(--gold);color:var(--ink);font-size:14px}
.follow{position:absolute;left:1046px;top:48px}
.follow ul{list-style:none;margin-top:12px;font-size:12px;line-height:28px;color:#a8dcb5}
.follow li{display:flex;align-items:center;gap:6px}
.follow li i{width:14px;height:14px;border-radius:2px;background:#2b6fb0}
.bottombar{top:3270px;height:76px;background:var(--green-dark);color:var(--white);text-align:center;font-size:13px;line-height:76px}
</style>
</head>
<body>

<div class="wrap topbar">
  <div class="contact">
    <span><svg width="12" height="12" viewBox="0 0 24 24"><path fill="#fff" d="M6.6 10.8a15 15 0 0 0 6.6 6.6l2.2-2.2c.3-.3.7-.4 1-.2 1.1.4 2.3.6 3.6.6.6 0 1 .4 1 1V20c0 .6-.4 1-1 1A17 17 0 0 1 3 4c0-.6.4-1 1-1h3.5c.6 0 1 .4 1 1 0 1.3.2 2.5.6 3.6.1.3 0 .7-.2 1z"/></svg>1.800.555.0142</span>
    <span><svg width="13" height="10" viewBox="0 0 26 20"><path fill="#fff" d="M0 0h26v20H0z"/><path fill="none" stroke="#3ea55b" stroke-width="2" d="M1 1l12 10L25 1"/></svg>info@veltromark.com</span>
  </div>
  <div class="checkout">Check Out <svg width="14" height="12" viewBox="0 0 28 24"><path fill="#fff" d="M0 0h5l2 4h21l-4 10H9zM10 18a3 3 0 1 1 0 6 3 3 0 0 1 0-6zm12 0a3 3 0 1 1 0 6 3 3 0 0 1 0-6z"/></svg></div>
</div>

<header class="wrap header">
  <div class="brand"><span class="dot"></span><span class="name">Veltromark</span></div>
  <nav class="nav"><span class="active">Home</span><span>About Us</span><span>How It Works</span><span>Benefits</span></nav>
</header>

<section class="wrap hero" role="img" aria-label="Photo of a smiling female doctor and a senior man giving a thumbs up">
  <div class="hero-copy">
    <div class="kicker">Help Protect</div>
    <h1>Our Seniors</h1>
    <p>Do your part in advancing safety and HIPAA compliance in Senior Living Communities</p>
    <span class="btn-outline">Register Here</span>
  </div>
  <div class="dots"><i></i><i></i><i></i><i></i></div>
</section>

<section class="wrap intro">
  <h2 class="section-title">Know your vendors</h2>
  <p>Veltromark is a front entry, digital, sign-in kiosk that screens and verifies third-party vendors and service providers. This proprietary technology verifies with a photo that every third party vendor and service provider meets community specific requirements before a badge is printed and entry is granted.</p>
  <span class="btn">Learn More</span>
</section>

<h2 class="row-title" style="top:800px">Vendors &amp; Care Providers</h2>
<div class="carousel-arrows">
  <svg width="10" height="16" viewBox="0 0 10 16"><path d="M8 2L2 8l6 6" fill="none" stroke="#222" stroke-width="2.5"/></svg>
  <svg width="10" height="16" viewBox="0 0 10 16"><path d="M2 2l6 6-6 6" fill="none" stroke="#222" stroke-width="2.5"/></svg>
</div>
<div class="people" style="top:883px">
  <div class="person" style="left:150px"><div class="portrait light" role="img" aria-label="Portrait of a hospice nurse"></div>Hospice Provider</div>
  <div class="person" style="left:453px"><div class="portrait light" role="img" aria-label="Portrait of a home care nurse"></div>Home Care Provider</div>
  <div class="person" style="left:765px"><div class="portrait dark" role="img" aria-label="Portrait of a medical equipment technician"></div>DME Provider</div>
  <div class="person" style="left:1048px"><div class="portrait light" role="img" aria-label="Portrait of a home health aide"></div>Home Health Provider</div>
</div>

<section class="wrap video" role="img" aria-label="Video still of a caregiver speaking with a senior resident">
  <div class="shade"></div>
  <h2>How Veltromark Works</h2>
  <svg width="112" height="112" viewBox="0 0 112 112"><circle cx="56" cy="56" r="50" fill="none" stroke="#fff" stroke-width="8"/><path d="M44 32l34 24-34 24z" fill="#fff"/></svg>
</section>

<h2 class="row-title" style="top:1570px">Veltromark Benefits</h2>
<div class="benefit" style="left:214px">
  <div class="icon"><svg width="60" height="52" viewBox="0 0 60 52"><path fill="#fff" d="M30 2L2 26h8v24h14V36h12v14h14V26h8z"/></svg></div>
  <h3>Community</h3>
  <p>Receive alerts when caregivers do not meet community standards, appointment times, and other critical requirements.</p>
</div>
<div class="benefit" style="left:589px">
  <div class="icon"><svg width="40" height="60" viewBox="0 0 40 60"><circle cx="20" cy="8" r="7" fill="#fff"/><path fill="#fff" d="M2 18h36v6H27v34h-6V40h-2v18h-6V24H2z"/></svg></div>
  <h3>Family</h3>
  <p>Receive alerts when caregivers do not meet community standards, appointment times, and other critical requirements.</p>
</div>
<div class="benefit" style="left:966px">
  <div class="icon"><svg width="56" height="64" viewBox="0 0 56 64"><path d="M8 4v18a12 12 0 0 0 24 0V4M20 34v12a12 12 0 0 0 24 0V32" fill="none" stroke="#fff" stroke-width="5"/><circle cx="44" cy="24" r="7" fill="none" stroke="#fff" stroke-width="5"/></svg></div>
  <h3>Vendor</h3>
  <p>Receive alerts when caregivers do not meet community standards, appointment times, and other critical requirements.</p>
</div>

<h2 class="row-title" style="top:2055px">Management Team</h2>
<div class="people" style="top:2139px">
  <div class="person" style="left:150px"><div class="portrait dark" role="img" aria-label="Portrait of Glen Hartley"></div>Glen Hartley</div>
  <div class="person" style="left:453px"><div class="portrait dark" role="img" aria-label="Portrait of Walter Price"></div>Walter Price</div>
  <div class="person" style="left:765px"><div class="portrait dark" role="img" aria-label="Portrait of Derek Sloane"></div>Derek Sloane</div>
  <div class="person" style="left:1048px"><div class="portrait dark" role="img" aria-label="Portrait of Owen Castell"></div>Owen Castell</div>
</div>

<section class="wrap testimonial" role="img" aria-label="Background photo of a senior couple smiling together">
  <div class="shade"></div>
  <div class="inner">
    <h2>Testimonial</h2>
    <p>Sed ut perspiciatis unde omnis iste natus error sit voluptatem accusantium doloremque laudantium, totam rem aperiam, eaque ipsa quae ab illo inventore veritatis et quasi architecto beatae vitae dicta sunt explicabo.</p>
    <cite>- Lorem ipsum dolor-</cite>
  </div>
</section>

<section class="wrap partners" aria-label="Partner communities">
  <div class="partner" style="width:112px;height:44px;border-radius:22px"></div>
  <div class="partner" style="width:124px;height:52px;border-radius:6px"></div>
  <div class="partner" style="width:118px;height:80px"></div>
  <div class="partner" style="width:144px;height:44px;border-radius:6px"></div>
  <div class="partner" style="width:144px;height:64px;border-radius:6px"></div>
</section>

<footer class="wrap footer">
  <div class="brand"><span class="dot"></span><span class="name">Veltromark</span></div>
  <div class="quick">
    <h4>Quick Links</h4>
    <ul><li>Home</li><li>About Us</li><li>How It Works</li><li>Benefits</li></ul>
  </div>
  <div class="newsletter">
    <h4>Subscribe Our Newsletter</h4>
    <p>Sed ut perspiciatis unde omnis iste natus error sit voluptatem accusantium doloremque</p>
    <div class="field"></div>
    <span class="submit">Submit</span>
  </div>
  <div class="follow">
    <h4>Follow us</h4>
    <ul>
      <li><i></i>Friendsy</li>
      <li><i style="background:#4fb3e6"></i>Chirper</li>
      <li><i style="background:#f39a1e"></i>Rss</li>
      <li><i></i>Circlo Plus</li>
    </ul>
  </div>
</footer>
<div class="wrap bottombar">© 2014 veltromark.com. All rights reserved.</div>

</body>
</html>
```